Website Redesign project for agency

we're looking to see some new designs for an agency website.
details in this google doc: https://files.brindlepath.example/sheet/d/7QXvRk2PaLw9HsNe4TyUc8JbZoMf3Gd61572-qKrA9w/view?mode=shared
homepage and one inner page/ or the blog page
please visit the google doc above to see the website that needs to be redesigned as well as an example website we like.
if you have any questions please send them to us asap
thank you
Target Market(s)
small business owners
Number of Pages Required
2 page
Font styles to use
Sans Serif
Requirements
Nice to have
- custom design
Should not have
- do not use a template you find online

```html
<!DOCTYPE html>
<html lang="en">
<head>
<meta charset="utf-8">
<title>Loop &amp; Rally — Digital Agency</title>
<link href="https://fonts.googleapis.com/css2?family=Hind:wght@400;500;600;700&family=Nunito+Sans:wght@400;600;700&display=swap" rel="stylesheet">
<style>
:root{
  --purple:#5b22d4;
  --purple-deep:#4a1db3;
  --purple-light:#8b3fe3;
  --lavender:#ece8fb;
  --ink:#1c1530;
  --body:#3d3850;
  --muted:#6b6680;
  --white:#ffffff;
  --black:#0d0a14;
}
*{margin:0;padding:0;box-sizing:border-box}
html,body{width:1200px;height:5021px;overflow:hidden}
body{position:relative;font-family:"Nunito Sans",sans-serif;color:var(--body);background:var(--white)}
.abs{position:absolute}
h1,h2,h3{font-family:"Hind",sans-serif;color:var(--ink)}

/* hero */
.hero{position:absolute;left:0;top:0;width:1200px;height:668px;background:linear-gradient(120deg,var(--purple) 0%,#6a2bd8 55%,var(--purple-light) 100%)}
.brand{font-family:"Hind",sans-serif;font-weight:700;color:var(--white);font-size:24px;letter-spacing:.5px}
.nav{position:absolute;top:34px;left:615px;display:flex;gap:30px;align-items:center;font-size:12px;color:var(--white);letter-spacing:.5px}
.nav .pill{border:1px solid rgba(255,255,255,.6);background:rgba(255,255,255,.18);border-radius:20px;padding:8px 18px}
.hero h1{position:absolute;left:115px;top:180px;width:520px;color:var(--white);font-size:50px;line-height:54px;font-weight:700}
.hero .lede{position:absolute;left:115px;top:358px;width:450px;color:var(--white);font-size:14.5px;line-height:21px}
.btn{position:absolute;display:flex;align-items:center;justify-content:center;border-radius:30px;font-size:17px}
.btn-white{background:var(--white);color:var(--purple)}
.btn-ghost{border:2px solid var(--white);color:var(--white)}
.hero-photo{position:absolute;left:610px;top:100px;width:470px;height:568px}

/* sections */
.section-title{position:absolute;left:0;width:1200px;text-align:center;font-size:56px;font-weight:700;line-height:60px}
.rule{position:absolute;left:540px;width:120px;height:4px;background:var(--purple);border-radius:2px}
.about-text{position:absolute;left:588px;top:893px;width:500px;font-size:13.5px;line-height:28.5px;color:var(--body)}
.about-text p+p{margin-top:28px}

.services{position:absolute;left:0;top:1355px;width:1200px;height:670px;background:var(--lavender)}
.card{position:absolute;top:1555px;width:306px;height:390px;border-radius:6px;text-align:center}
.card.active{background:var(--purple)}
.card .icon{position:absolute;left:93px;top:25px;width:120px;height:130px;border-radius:16px;background:linear-gradient(135deg,#d8cdfa,#9f7de8)}
.card h3{position:absolute;top:195px;left:0;width:100%;font-family:"Nunito Sans",sans-serif;font-weight:400;font-size:38px}
.card p{position:absolute;top:248px;left:40px;width:226px;font-size:13px;line-height:27px;color:var(--body)}
.card .more{position:absolute;top:325px;left:83px;width:140px;height:36px;border:2px solid var(--purple);border-radius:20px;font-size:14px;color:var(--purple);display:flex;align-items:center;justify-content:center}
.card.active h3,.card.active p{color:var(--white)}
.card.active .more{background:var(--white);border-color:var(--white)}

.works-intro{position:absolute;left:115px;top:2226px;width:970px;text-align:center;font-size:19px;line-height:35px;color:var(--ink)}
.work{position:absolute;width:473px;height:354px;box-shadow:0 2px 8px rgba(0,0,0,.12)}
.outline-btn{position:absolute;border:2px solid var(--purple);border-radius:30px;color:var(--purple);font-size:18px;display:flex;align-items:center;justify-content:center;gap:8px}

.clients-intro{position:absolute;left:115px;top:3434px;width:970px;text-align:center;font-size:19.5px;line-height:35px;color:var(--ink)}
.client-mark{position:absolute;top:3615px;width:273px;text-align:center;font-family:"Nunito Sans",sans-serif;font-weight:700;font-size:17px;color:var(--ink);display:flex;align-items:center;justify-content:center;gap:8px}
.client-mark i{display:inline-block;width:18px;height:18px;background:var(--ink)}
.quote{position:absolute;top:3693px;width:274px;height:488px;border:1.5px solid var(--purple);border-radius:16px;text-align:center}
.quote .avatar{position:absolute;left:95px;top:34px;width:84px;height:84px;border-radius:50%;background:linear-gradient(160deg,#c9c3d6,#5b5570)}
.quote blockquote{position:absolute;left:22px;top:140px;width:230px;font-size:12.5px;line-height:21.5px;color:var(--body)}
.quote .name{position:absolute;left:10px;top:407px;width:254px;font-weight:700;font-size:13px;color:var(--ink)}
.quote .role{position:absolute;left:10px;top:428px;width:254px;font-size:9.5px;line-height:14px;color:var(--muted)}

.cta{position:absolute;left:0;top:4262px;width:1200px;height:338px;background:var(--lavender)}
.cta h2{position:absolute;left:100px;top:82px;width:1000px;text-align:center;font-family:"Nunito Sans",sans-serif;font-weight:400;font-size:42px;line-height:48px}
.btn-solid{background:var(--purple);color:var(--white)}

.footer{position:absolute;left:0;top:4600px;width:1200px;height:396px;background:var(--purple-deep);color:var(--white)}
.footer h4{font-family:"Nunito Sans",sans-serif;font-weight:700;font-size:17px;text-align:center}
.footer p{font-size:13px;line-height:19px;text-align:center}
.social{display:flex;gap:22px}
.social span{width:44px;height:44px;border-radius:50%;background:rgba(255,255,255,.35)}
.legal{position:absolute;left:0;top:4996px;width:1200px;height:25px;background:var(--black);color:#bbb;font-size:9px;text-align:center;line-height:25px}
</style>
</head>
<body>

<!-- Hero -->
<header class="hero">
  <div class="brand abs" style="left:115px;top:30px">LOOP &amp; RALLY</div>
  <nav class="nav">
    <span>WHAT WE DO ⌄</span><span>PROJECTS</span><span>WHO WE ARE ⌄</span><span class="pill">BOOK US</span>
  </nav>
  <h1>A One-Stop Solution for Your Company Digital Needs</h1>
  <p class="lede">Whether you need a new Website, SEO, Social Media or marketing plan, we're up for the task</p>
  <a class="btn btn-white" style="left:118px;top:440px;width:164px;height:55px">Book Us</a>
  <a class="btn btn-ghost" style="left:297px;top:440px;width:161px;height:55px">Our Works</a>
  <svg class="hero-photo" viewBox="0 0 470 568" role="img" aria-label="Photo of a smiling woman holding a tablet">
    <path d="M150 120 C230 40 360 60 400 170 C440 280 470 400 420 480 C380 540 300 520 250 460 C200 400 90 380 70 300 C55 230 100 170 150 120Z" fill="#9b5ce8" opacity=".55"/>
    <rect x="140" y="0" width="230" height="568" rx="110" fill="#6b3a52" opacity=".55"/>
  </svg>
</header>

<!-- Who we are -->
<h2 class="section-title" style="top:748px">Who We Are</h2>
<div class="rule" style="top:823px"></div>
<svg class="abs" style="left:115px;top:870px" width="400" height="405" viewBox="0 0 400 405" role="img" aria-label="Photo of two colleagues working on a laptop">
  <path d="M40 20 C150 -10 300 20 370 60 C420 100 390 200 330 290 C270 380 200 410 150 370 C90 320 20 250 10 160 C0 90 10 30 40 20Z" fill="#c9a98a"/>
  <path d="M50 30 C160 0 310 30 380 70 C430 110 400 210 340 300 C280 390 210 420 160 380" fill="none" stroke="var(--purple)" stroke-width="2"/>
</svg>
<div class="about-text">
  <p>Whether you need a new Website, SEO, Social Media or marketing plan, we're up for the task. Loop &amp; Rally has a team of talented developers, designers &amp; inbound marketers at your disposal. We'll help you own your local or national market within your industry.</p>
  <p>We're the most reviewed and highest rated Web Design company in Millbrook that focuses on services that include inbound marketing, search engine optimization, social media marketing, lead conversion, to nurturing, and marketing automation. We perform high-end mobile-friendly web design, content creation, SEO, social media strategy development, email marketing, and more. Our clients in Millbrook and around the country enjoy more website visitors, more conversions, and best of all a better return on investment.</p>
</div>

<!-- What we do -->
<section class="services"></section>
<h2 class="section-title" style="top:1433px">What We Do</h2>
<div class="rule" style="top:1508px"></div>
<div class="card" style="left:115px">
  <div class="icon" role="img" aria-label="Web design illustration"></div>
  <h3>Web Design</h3>
  <p>We Design to Convert Site Visitors Into Customers.</p>
  <div class="more">Learn More</div>
</div>
<div class="card active" style="left:441px">
  <div class="icon" role="img" aria-label="SEO growth chart illustration"></div>
  <h3>SEO</h3>
  <p>Search Engine Optimization for More Traffic.</p>
  <div class="more">Learn More</div>
</div>
<div class="card" style="left:767px">
  <div class="icon" role="img" aria-label="Social media sharing illustration"></div>
  <h3>Social Media</h3>
  <p>Engage in Coversation With Customers Online</p>
  <div class="more">Learn More</div>
</div>

<!-- Our works -->
<h2 class="section-title" style="top:2105px">Our Works</h2>
<p class="works-intro">Loop &amp; Rally has produced websites for dentists, consulting, healthcare, financial service companies, and more</p>
<div class="work" role="img" aria-label="Home builder website project" style="left:115px;top:2337px;background:linear-gradient(180deg,#7c5cc8,#a58fde)"></div>
<div class="work" role="img" aria-label="Roofing company website project" style="left:612px;top:2337px;background:linear-gradient(180deg,#e9eef3,#8e9aa8)"></div>
<div class="work" role="img" aria-label="Kitchen and bath website project" style="left:115px;top:2714px;background:linear-gradient(180deg,#4a4a52 0%,#6d6a72 55%,#f6f6f6 56%)"></div>
<div class="work" role="img" aria-label="Children's music program website project" style="left:612px;top:2714px;background:linear-gradient(180deg,#f5f08a 0%,#5f7fd6 40%,#e8b08a 100%)"></div>
<a class="outline-btn" style="left:498px;top:3107px;width:204px;height:55px">View All Works <span>→</span></a>

<!-- Testimonials -->
<h2 class="section-title" style="top:3244px;line-height:68px">Happy Clients<br>Says It All</h2>
<div class="rule" style="top:3392px"></div>
<p class="clients-intro">We do a lot more than just build awesome websites. We partner with all our clients to build relationships and create marketing plans that help them improve their business. But don't just take our word for it. See what our clients have to say.</p>

<div class="client-mark" style="left:148px">KEYSTONE LEDGER</div>
<div class="client-mark" style="left:480px"><i></i>NORTHFIELD</div>
<div class="client-mark" style="left:811px"><i></i>HARBOR LIGHTS</div>

<div class="quote" style="left:148px">
  <div class="avatar" role="img" aria-label="Client portrait"></div>
  <blockquote>"Grant and his team were incredibly responsive, resourceful, and diligent. Grant specifically translated "non-web savvy" ideas promoted by us, into a site that exceeded our expectations. We would recommend Loop &amp; Rally to anyone considering anything to do with website design, SEO, and marketing!"</blockquote>
  <div class="name">Marcus Delaney</div>
  <div class="role">Managing Member, Keystone Ledger Partners</div>
</div>
<div class="quote" style="left:480px">
  <div class="avatar" role="img" aria-label="Client portrait"></div>
  <blockquote>"Grant Holloway at Loop &amp; Rally has been terrific to work with. Grant provided valuable direction and insight. If you are looking for creative talent and strategic direction, Loop &amp; Rally is a good place to start."</blockquote>
  <div class="name">Owen Whitfield</div>
  <div class="role">Founder &amp; CEO, Northfield Care Group</div>
</div>
<div class="quote" style="left:811px">
  <div class="avatar" role="img" aria-label="Client portrait"></div>
  <blockquote>"Loop &amp; Rally just redesigned our nonprofit website and we couldn't be happier with the results. The team is very pleasing to work with, professional, responsive to our requests and always made sure that the product met our expectations. I would definitely recommend Loop &amp; Rally to anyone looking to create or redesign their website!"</blockquote>
  <div class="name">Daniela M. Ortiz-Vega, MD</div>
  <div class="role">Secretary &amp; Chief Operational Officer, Harbor Lights Collective</div>
</div>

<!-- CTA -->
<section class="cta">
  <h2>Ready To Make a Real Change? Let's Build this Thing Together!</h2>
  <a class="btn btn-solid" style="left:462px;top:206px;width:233px;height:52px">Book Us Now</a>
</section>

<!-- Footer -->
<footer class="footer">
  <div class="brand abs" style="left:145px;top:98px">LOOP &amp; RALLY</div>
  <p class="abs" style="left:112px;top:140px;width:230px">Ready to start a new project or curious about our process? Drop us a note or give us a call. We are happy to answer any questions and provide a free consultation.</p>

  <div class="abs" style="left:417px;top:100px;width:200px">
    <h4>Hours</h4>
    <p style="margin-top:6px">Monday - Saturday<br>8 AM - 8 PM</p>
    <h4 style="margin-top:26px">Location</h4>
    <p style="margin-top:6px">Millbrook Website<br>Design<br>18 Linden Row #204,<br>Millbrook, MA 02190<br>555-013-4827</p>
  </div>

  <div class="abs" style="left:700px;top:100px;width:390px">
    <h4>Connect</h4>
    <div class="social" style="margin-top:18px;margin-left:0" aria-label="Social profiles"><span></span><span></span><span></span><span></span><span></span></div>
    <div style="margin-top:22px;display:flex;align-items:center;justify-content:center;gap:10px;font-weight:700;font-size:18px">
      <svg width="20" height="20" viewBox="0 0 24 24" aria-hidden="true"><path fill="#fff" d="M6.6 10.8a15.1 15.1 0 0 0 6.6 6.6l2.2-2.2c.3-.3.7-.4 1-.2 1.1.4 2.3.6 3.6.6.6 0 1 .4 1 1V20c0 .6-.4 1-1 1A17 17 0 0 1 3 4c0-.6.4-1 1-1h3.5c.6 0 1 .4 1 1 0 1.3.2 2.5.6 3.6.1.3 0 .7-.2 1z"/></svg>
      555-013-4827
    </div>
  </div>
</footer>
<div class="legal">©2020 LOOP &amp; RALLY</div>

</body>
</html>
```